Digital One Pager for Consulting Practice

I would like the essence of the content in my ppt consolidated into a one-pager. The one-pager will mainly be sent via email as a pdf and intended to excite and invite new clients and establish the credibility of my boutique high-end consulting firm. Infographics and symbols would be a plus. The target client should view the firm as providing premeir service. The client is getting a thought partner.

Target Market(s)

Large Medical Device Manufacturer Executives, Early-Stage Medical Device Manufacturer Executives, Partners at VC Firms

Industry/Entity Type

Medical Equipment

Colors
0355a3
f37122

Requirements
Must have
• Please match the color scheme in ppt. Please use the existing logo. I am very open to better graphics on the process. My photo does not need to be on the digital flyer. Hyper link to the website and email is needed.
Nice to have
• Infographics

```html
<!DOCTYPE html>
<html lang="en">
<head>
<meta charset="utf-8">
<title>Halvern Advisory – One Pager</title>
<link href="https://fonts.googleapis.com/css2?family=Montserrat:wght@400;500;600&family=Roboto+Condensed:wght@400;500;700&display=swap" rel="stylesheet">
<style>
:root{
  --navy:#1d2a57;
  --navy-deep:#14193a;
  --blue:#0355a3;
  --sky:#1e9ee3;
  --orange:#f37122;
  --red:#e2452c;
  --ink:#2a2a2a;
  --grey-band:#ececec;
  --grey-box:#e6e6e6;
  --teal:#4fc3e0;
  --bar:#3a5a9c;
  --backdrop:#dfe3ea;
}
*{margin:0;padding:0;box-sizing:border-box}
html,body{width:1200px;height:1200px;overflow:hidden;background:var(--backdrop)}
.page{position:absolute;left:136px;top:0;width:928px;height:1200px;background:#fff;font-family:"Roboto Condensed",sans-serif;color:var(--ink);overflow:hidden}
.abs{position:absolute}
.heading{font-family:"Montserrat",sans-serif;font-weight:400;color:var(--navy);font-size:36px;letter-spacing:.3px;white-space:nowrap}
.brand{left:596px;top:42px;display:flex;align-items:center;gap:12px}
.brand-mark{width:34px;height:34px;background:var(--orange)}
.brand-name{font-family:"Montserrat",sans-serif;font-weight:600;font-size:30px;color:var(--navy);letter-spacing:2px;line-height:37px}
.exp-list{left:83px;top:130px;font-size:16px;font-weight:500;line-height:20px}
.exp-list p{white-space:nowrap}
.exp-list .dot{color:var(--sky)}
.diff-box{position:absolute;border-radius:6px;font-size:20px;font-weight:500;display:flex;align-items:center;justify-content:center;background:var(--grey-box);color:#111}
.diff-box.lead{background:var(--navy);color:#fff;box-shadow:0 3px 6px rgba(0,0,0,.35);z-index:2}
.svc-title{font-size:15px;font-weight:500;color:var(--red);white-space:nowrap}
.svc-list{font-size:14.5px;line-height:18px;white-space:nowrap}
.band{left:0;top:556px;width:928px;height:259px;background:var(--grey-band)}
.sub-title{font-size:17px;font-weight:500;color:var(--sky);white-space:nowrap}
.sub-list{font-size:16px;line-height:20px}
.process{left:63px;top:779px;filter:drop-shadow(3px 4px 4px rgba(0,0,0,.3))}
.step{position:absolute;color:#fff;font-size:19px;font-weight:500;line-height:22px}
.partner-rule{top:908px;height:2px;background:#c9c9c9}
.partners{left:40px;top:955px;width:850px;display:flex;justify-content:space-between;align-items:center}
.partner{font-size:15px;font-weight:500;color:var(--navy);display:flex;align-items:center;gap:6px;white-space:nowrap}
.partner-sq{width:14px;height:14px;background:var(--blue)}
.footer-strip{left:0;top:1036px;width:928px;height:24px;background:var(--navy-deep)}
.footer{left:0;top:1060px;width:928px;height:140px;background:var(--navy)}
.footer-title{left:66px;top:1062px;font-family:"Montserrat",sans-serif;font-size:46px;color:#fff;white-space:nowrap}
.footer-bar{left:60px;top:1127px;width:543px;height:31px;background:var(--bar);color:#fff;font-family:"Montserrat",sans-serif;font-size:16.5px;display:flex;align-items:center;justify-content:center;white-space:nowrap}
.contact{left:652px;top:1075px;font-family:Arial,Helvetica,sans-serif;white-space:nowrap}
.contact a{color:var(--teal);text-decoration:none;font-size:21px;display:block}
.contact .phone{color:#fff;font-size:37px;line-height:44px}
</style>
</head>
<body>
<main class="page">
  <div class="abs brand"><span class="brand-mark"></span><span class="brand-name">HALVERN<br>ADVISORY</span></div>

  <h2 class="abs heading" style="left:83px;top:72px">Experience</h2>
  <div class="abs exp-list">
    <p><span class="dot">•</span>Over a decade &nbsp;@FDA (Former Deputy Division Director)</p>
    <p style="margin-top:21px"><span class="dot">•</span>Expertise: Cardiovascular, Ophthalmology, General Hospital, Infection Control, Dental, Anesthesia, Respiratory</p>
    <p style="margin-top:20px"><span class="dot">•</span>Vice President Regulatory Affairs / Quality Assurance @Corvell Industries (Fortune 150 Company)</p>
    <p style="font-weight:400">•Initiated &nbsp;reorganization of department &nbsp;&nbsp;•Led major compliance effort &nbsp;&nbsp;•Successful FDA inspection (no observations)</p>
  </div>

  <h2 class="abs heading" style="left:83px;top:304px">Differentiators</h2>
  <div class="diff-box" style="left:70px;top:368px;width:166px;height:52px;padding-bottom:8px">Experience</div>
  <div class="diff-box" style="left:253px;top:368px;width:167px;height:52px;padding-bottom:8px">Network</div>
  <div class="diff-box lead" style="left:161px;top:408px;width:167px;height:52px">Leverage</div>
  <div class="diff-box" style="left:175px;top:450px;width:140px;height:52px;padding-top:6px">Process</div>

  <h2 class="abs heading" style="left:507px;top:303px">Services</h2>
  <div class="abs svc-title" style="left:513px;top:357px">Regulatory Strategy</div>
  <div class="abs svc-list" style="left:513px;top:394px">•RAQA Organizational Structure<br>•Regulatory Pathway</div>
  <div class="abs svc-title" style="left:513px;top:449px">Interim Executive Leadership</div>
  <div class="abs svc-list" style="left:513px;top:486px">•Compliance Remediation<br>•Accelerated Product Registration</div>
  <div class="abs svc-title" style="left:752px;top:357px">FDA Communications</div>
  <div class="abs svc-list" style="left:752px;top:394px">•Deficiency Response<br>•Application Review</div>
  <div class="abs svc-title" style="left:752px;top:449px">Training</div>
  <div class="abs svc-list" style="left:752px;top:486px">•FDA Communication<br>•MDR Reporting</div>

  <div class="abs band"></div>
  <h2 class="abs heading" style="left:83px;top:574px">Experience to Provide...</h2>
  <div class="abs sub-title" style="left:84px;top:625px">Executive Application Review</div>
  <div class="abs sub-list" style="left:84px;top:646px">•Examples include: Presubmission, IDE, 510(k), 513(g),<br>&nbsp;&nbsp;PMA, Refuse to Accept, Hold letter<br>•Troubleshooting</div>
  <div class="abs sub-title" style="left:493px;top:625px">Strategic Advice &amp; Diligence to Investors</div>
  <div class="abs sub-list" style="left:493px;top:646px">•Validate &amp; Verify Founder Milestones<br>•Diligence portfolio company Regulatory and Quality systems</div>

  <h2 class="abs heading" style="left:83px;top:726px">Efficient Process</h2>
  <svg class="abs process" width="790" height="62" viewBox="0 0 790 62" role="img" aria-label="Four step process chevrons">
    <path d="M597 0H782a5 5 0 0 1 5 5V56a5 5 0 0 1-5 5H597Z" fill="#12224f"/>
    <path d="M407 0H597L615 30.5 597 61H407Z" fill="#0e3a7c"/>
    <path d="M182 0H407L425 30.5 407 61H182Z" fill="#0b5fb2"/>
    <path d="M5 0H182L200 30.5 182 61H5a5 5 0 0 1-5-5V5a5 5 0 0 1 5-5Z" fill="#1a9de2"/>
  </svg>
  <div class="step" style="left:101px;top:798px">Exploratory Call</div>
  <div class="step" style="left:290px;top:798px">Regulatory Landscape</div>
  <div class="step" style="left:505px;top:799px">Problem Statement</div>
  <div class="step" style="left:699px;top:788px">Review &amp; Align<br>on Deliverables</div>

  <div class="abs partner-rule" style="left:41px;width:185px"></div>
  <div class="abs partner-rule" style="left:702px;width:185px"></div>
  <h2 class="abs heading" style="left:249px;top:888px">Valued Partner Network</h2>
  <div class="abs partners">
    <span class="partner"><span class="partner-sq"></span>Westfield Tech Transfer</span>
    <span class="partner">Harbor Angels</span>
    <span class="partner">DeviceLab</span>
    <span class="partner">Ardent Quality Group</span>
    <span class="partner">Brandt Law Firm, PC</span>
    <span class="partner">PeopleCore</span>
  </div>

  <div class="abs footer-strip"></div>
  <div class="abs footer"></div>
  <div class="abs footer-title">Halvern Advisory Value</div>
  <div class="abs footer-bar">Extensive Experience &nbsp;&nbsp;| &nbsp;&nbsp;Efficient Process &nbsp;&nbsp;| &nbsp;&nbsp;Valued Network</div>
  <div class="abs contact">
    <a href="https://www.halvern.example">www.halvern.example</a>
    <div class="phone">202 555 0148</div>
    <a href="mailto:info@halvern.example">info@halvern.example</a>
  </div>
</main>
</body>
</html>
```